K & D A/C Compressors' Business Card

Hello,

I need someone to create a new business card for my business. The name of my Business is: K & D A/C Compressors. I sell automotive air conditioning parts (a/c parts). I would like the business card to incorporate my logo, and to have an automotive feel to it. It is important that the business card feel like it is coming from an automotive parts business.

I already have a logo, which I will provide.

Thanks.
Updates

Project Deadline Extended Reason: I feel like extending the deadline until October 9, 2017, will allow for more time to design the business card. Thank you for your understanding. Added Monday, October 2, 2017

Target Market(s)

Consumers who need automotive a/c parts, and auto mechanics.

Industry/Entity Type

Automotive

Contact Information for Business Card

Business name: K & D A/C Compressors
Business Address: 48207 Southwest 36th Street, Harbor Vale, Oregon 97418
Telephone: 555-472-1390
Fax: To be provided once I choose your design.
Website: www.kdcoolunits.example
Email: support@kdcoolunits.example
Names: To be provided once I choose your design.

Font styles to use
Sans Serif

Colors

Designer to choose colors to be used in the design.

Requirements
Must have
• The business card must include all of the "Business Card Details" and the logo I have uploaded.

```html
<!DOCTYPE html>
<html lang="en">
<head>
<meta charset="utf-8">
<title>K &amp; D A/C Compressors – Business Card</title>
<link rel="stylesheet" href="https://fonts.googleapis.com/css2?family=Montserrat:wght@300;400;700&display=swap">
<style>
  :root {
    --bg: #2a2c2f;
    --card: #ffffff;
    --brand-blue: #26aae1;
    --tint-blue: #dff0fa;
    --tint-blue-soft: #ffffff;
    --text-grey: #9a9ea3;
    --logo-grey: #8f9398;
  }
  * { box-sizing: border-box; margin: 0; padding: 0; }
  html, body {
    width: 1200px; height: 900px; overflow: hidden;
    background: var(--bg);
    font-family: "Montserrat", Arial, sans-serif;
  }
  .canvas { position: relative; width: 1200px; height: 900px; }

  .card {
    position: absolute;
    width: 720px; height: 411px;
    background: var(--card);
    box-shadow: 0 12px 30px rgba(0,0,0,.45);
    overflow: hidden;
  }
  .card--front { left: 120px; top: 36px; }
  .card--back  { left: 360px; top: 462px; }

  /* front */
  .front-pattern {
    position: absolute; inset: 0;
    background: linear-gradient(135deg, var(--tint-blue) 0%, var(--tint-blue-soft) 45%, var(--tint-blue) 100%);
  }
  .wordmark {
    display: flex; align-items: center; gap: 14px;
    color: var(--logo-grey); font-weight: 400;
    white-space: nowrap;
  }
  .wordmark__square { width: 22px; height: 22px; background: var(--brand-blue); flex: none; }
  .card--front .wordmark {
    position: absolute; left: 50%; top: 50%;
    transform: translate(-50%, -50%);
    font-size: 38px;
  }

  /* back */
  .back-band {
    position: absolute; left: 0; top: 0; bottom: 0; width: 78px;
    background: var(--brand-blue);
  }
  .back-content { position: absolute; left: 120px; top: 40px; right: 40px; }
  .card--back .wordmark { font-size: 28px; }
  .person { margin-top: 30px; }
  .person__name { color: var(--brand-blue); font-weight: 700; font-size: 22px; letter-spacing: .5px; }
  .person__title { color: var(--text-grey); font-weight: 400; font-size: 15px; margin-top: 2px; }
  .contacts { list-style: none; margin-top: 22px; }
  .contacts li {
    display: flex; align-items: center; gap: 14px;
    color: var(--text-grey); font-size: 15px; font-weight: 400;
    line-height: 26px;
  }
  .contacts svg { width: 14px; height: 14px; fill: var(--brand-blue); flex: none; }
  .address {
    margin-top: 18px; margin-left: 28px;
    color: var(--text-grey); font-size: 15px; line-height: 21px;
  }
</style>
</head>
<body>
<div class="canvas">

  <section class="card card--front">
    <div class="front-pattern" role="img" aria-label="Faint light-blue repeating brand pattern across the card"></div>
    <div class="wordmark"><span class="wordmark__square"></span>K &amp; D A/C Compressors</div>
  </section>

  <section class="card card--back">
    <div class="back-band"></div>
    <div class="back-content">
      <div class="wordmark"><span class="wordmark__square"></span>K &amp; D A/C Compressors</div>
      <div class="person">
        <div class="person__name">MR. DANIEL</div>
        <div class="person__title">Creative GM</div>
      </div>
      <ul class="contacts">
        <li>
          <svg viewBox="0 0 24 24"><path d="M6.6 10.8a15.1 15.1 0 0 0 6.6 6.6l2.2-2.2a1 1 0 0 1 1-.25 11.4 11.4 0 0 0 3.6.57 1 1 0 0 1 1 1V20a1 1 0 0 1-1 1A17 17 0 0 1 3 4a1 1 0 0 1 1-1h3.5a1 1 0 0 1 1 1c0 1.25.2 2.45.57 3.6a1 1 0 0 1-.25 1z"/></svg>
          555-472-1390
        </li>
        <li>
          <svg viewBox="0 0 24 24"><path d="M6 2h12v5H6zM3 8h18a1 1 0 0 1 1 1v8h-4v5H6v-5H2V9a1 1 0 0 1 1-1zm5 7v5h8v-5z"/></svg>
          555-472-1391
        </li>
        <li>
          <svg viewBox="0 0 24 24"><path d="M12 2a10 10 0 1 0 0 20 10 10 0 0 0 0-20zm6.9 6h-3a15 15 0 0 0-1.3-3.9A8 8 0 0 1 18.9 8zM12 4a13 13 0 0 1 1.9 4h-3.8A13 13 0 0 1 12 4zM4.3 14a8 8 0 0 1 0-4h3.4a16 16 0 0 0 0 4zm.8 2h3a15 15 0 0 0 1.3 3.9A8 8 0 0 1 5.1 16zm3-8h-3a8 8 0 0 1 4.3-3.9A15 15 0 0 0 8.1 8zM12 20a13 13 0 0 1-1.9-4h3.8A13 13 0 0 1 12 20zm2.3-6H9.7a14 14 0 0 1 0-4h4.6a14 14 0 0 1 0 4zm.3 5.9a15 15 0 0 0 1.3-3.9h3a8 8 0 0 1-4.3 3.9zm1.7-5.9a16 16 0 0 0 0-4h3.4a8 8 0 0 1 0 4z"/></svg>
          www.kdcoolunits.example
        </li>
        <li>
          <svg viewBox="0 0 24 24"><path d="M12 2a10 10 0 1 0 0 20v-2a8 8 0 1 1 8-8v1a2 2 0 0 1-4 0V7h-2v1a5 5 0 1 0 1 6.9A4 4 0 0 0 22 13v-1A10 10 0 0 0 12 2zm0 13a3 3 0 1 1 0-6 3 3 0 0 1 0 6z"/></svg>
          support@kdcoolunits.example
        </li>
      </ul>
      <p class="address">48207 Southwest 36th Street,<br>Harbor Vale, Oregon 97418</p>
    </div>
  </section>

</div>
</body>
</html>
```